New business card/stationary for a consulting company

I am looking for a clean and very professional looking business card for my consulting company as well as corresponding stationary. I am uploading our logo. I like simple and powerful for the feel. No graphics but I am open on everything else. Below is my contact information but would like the final to be in a version I can add my employees information into and print. Thank you.

Daniel Whitcombe
dan@fernlowadvisory.com
2837 North 9th Avenue, Summit Floor, Larkfield, Westmere 60483
www.fernlowadvisory.com

Industry/Entity Type

Consulting

Contact Information for Business Card

Daniel Whitcombe
dan@fernlowadvisory.com
www.fernlowadvisory.com

Font styles to use
Serif
Sans Serif

Requirements
Must have
• Our logo and the business card details.
Nice to have
• our website www.fernlowadvisory.com

```html
<!DOCTYPE html>
<html lang="en">
<head>
<meta charset="utf-8">
<title>Fernlow Advisory – Business Card</title>
<link href="https://fonts.googleapis.com/css2?family=Arimo:wght@400;700&display=swap" rel="stylesheet">
<style>
  :root {
    --brand-blue: #0a0fa8;
    --brand-blue-dark: #060a82;
    --band-grey: #8e8e92;
    --card-white: #f7f7f8;
    --canvas-bg: #e6e8ec;
    --text-white: #ffffff;
  }
  * { box-sizing: border-box; margin: 0; padding: 0; }
  html, body {
    width: 1200px; height: 900px; overflow: hidden;
    background: var(--canvas-bg);
    font-family: "Arimo", Arial, sans-serif;
  }
  .canvas { position: relative; width: 1200px; height: 900px; }
  .card {
    position: absolute; left: 300px;
    width: 600px; height: 343px;
    overflow: hidden;
    box-shadow: 0 10px 28px rgba(20, 24, 60, 0.22);
  }

  /* Back side */
  .card-back {
    top: 76px;
    background: radial-gradient(ellipse at 50% 40%, var(--brand-blue) 0%, var(--brand-blue-dark) 100%);
  }
  .card-back .grey-strip {
    position: absolute; left: 0; right: 0; bottom: 0; height: 40px;
    background: var(--band-grey);
  }
  .card-back .brand {
    position: absolute; top: 110px; left: 0; right: 0;
    display: flex; align-items: center; justify-content: center; gap: 16px;
    color: var(--text-white);
  }
  .brand-square { width: 34px; height: 34px; flex: none; }
  .card-back .brand-square { background: var(--card-white); }
  .brand-name {
    font-weight: 400; font-size: 34px; letter-spacing: 3px; text-transform: uppercase;
  }
  .card-back .website {
    position: absolute; top: 230px; left: 0; right: 0;
    text-align: center; color: var(--text-white);
    font-size: 15px; letter-spacing: 0.3px;
  }

  /* Front side */
  .card-front { top: 481px; background: var(--card-white); }
  .card-front .brand {
    position: absolute; top: 52px; right: 34px;
    display: flex; align-items: center; gap: 12px;
    color: var(--brand-blue);
  }
  .card-front .brand-square { width: 26px; height: 26px; background: var(--brand-blue); }
  .card-front .brand-name { font-size: 25px; letter-spacing: 2px; }
  .card-front .holder-name {
    position: absolute; top: 150px; left: 40px;
    color: var(--brand-blue); font-weight: 700;
    font-size: 22px; letter-spacing: 0.5px; text-transform: uppercase;
  }
  .contact-band { position: absolute; left: 0; top: 0; width: 600px; height: 343px; }
  .contact-list {
    position: absolute; left: 40px; top: 222px;
    list-style: none; color: var(--text-white); font-size: 14.5px;
  }
  .contact-list li { display: flex; align-items: center; gap: 10px; height: 22px; }
  .contact-icon { width: 16px; height: 16px; flex: none; }
  .office-address {
    position: absolute; right: 34px; top: 222px;
    color: var(--text-white); font-style: normal;
    font-size: 14.5px; line-height: 22px; text-align: right;
  }
</style>
</head>
<body>
<main class="canvas">

  <section class="card card-back" aria-label="Business card, back">
    <div class="brand">
      <span class="brand-square"></span>
      <span class="brand-name">Fernlow Advisory</span>
    </div>
    <p class="website">www.fernlowadvisory.com</p>
    <div class="grey-strip"></div>
  </section>

  <section class="card card-front" aria-label="Business card, front">
    <svg class="contact-band" viewBox="0 0 600 343" aria-hidden="true">
      <defs>
        <linearGradient id="bandBlue" x1="0" y1="0" x2="1" y2="0">
          <stop offset="0" stop-color="#0a0fa8"/>
          <stop offset="1" stop-color="#070b8e"/>
        </linearGradient>
      </defs>
      <path d="M0 200 H88 L100 214 L112 200 H600 V343 H0 Z" fill="url(#bandBlue)"/>
      <rect x="0" y="308" width="600" height="35" fill="#8e8e92"/>
    </svg>

    <div class="brand">
      <span class="brand-square"></span>
      <span class="brand-name">Fernlow Advisory</span>
    </div>

    <h1 class="holder-name">Daniel Whitcombe</h1>

    <ul class="contact-list">
      <li>
        <svg class="contact-icon" viewBox="0 0 16 16" aria-hidden="true">
          <rect width="16" height="16" rx="3" fill="#fff"/>
          <path d="M5 3.5 L6.8 5.6 L5.9 7 Q7 9.2 9 10.1 L10.4 9.2 L12.5 11 L11.3 12.6 Q7.5 12.4 4.6 8.6 Q3.4 6.2 3.7 4.6 Z" fill="#0a0fa8"/>
        </svg>
        555-310-42-86
      </li>
      <li>
        <svg class="contact-icon" viewBox="0 0 16 16" aria-hidden="true">
          <rect width="16" height="16" rx="3" fill="#fff"/>
          <rect x="3" y="4.5" width="10" height="7" fill="none" stroke="#0a0fa8" stroke-width="1.3"/>
          <path d="M3 4.8 L8 8.6 L13 4.8" fill="none" stroke="#0a0fa8" stroke-width="1.3"/>
        </svg>
        dan@fernlowadvisory.com
      </li>
      <li>
        <svg class="contact-icon" viewBox="0 0 16 16" aria-hidden="true">
          <rect width="16" height="16" rx="3" fill="#fff"/>
          <circle cx="8" cy="8" r="4.8" fill="none" stroke="#0a0fa8" stroke-width="1.2"/>
          <ellipse cx="8" cy="8" rx="2" ry="4.8" fill="none" stroke="#0a0fa8" stroke-width="1"/>
          <path d="M3.2 8 H12.8" stroke="#0a0fa8" stroke-width="1"/>
        </svg>
        www.fernlowadvisory.com
      </li>
    </ul>

    <address class="office-address">
      2837 North 9th Avenue<br>
      Summit Floor, Larkfield<br>
      Westmere 60483
    </address>
  </section>

</main>
</body>
</html>
```